VelloPath Business Card

Our company is called VelloPath and we are based in Tel Aviv, Israel. We create innovative and exciting methods for getting people on the web engaged with content. We need a cool yet professional business card that will represent our management level employees. keep in mind this is a start up company with a young atmosphere. You can be inspired by our logo (file attached, make sure you have the right font "Ubuntu-Condensed") Use the colors that are used in the logo and create a colourful and professional business card.

```html
<!DOCTYPE html>
<html lang="en">
<head>
<meta charset="utf-8">
<title>VelloPath Business Card</title>
<link rel="stylesheet" href="https://fonts.googleapis.com/css2?family=Ubuntu+Condensed&family=Playfair+Display:wght@700&family=Varela+Round&display=swap">
<style>
  :root {
    --stage: #e6e6e6;
    --paper: #ffffff;
    --brand-blue: #1b95d3;
    --deep-blue: #137bb3;
    --name-blue: #0f6ea3;
    --ink: #1a1a1a;
    --accent-yellow: #f5d020;
    --accent-pink: #e8308c;
    --accent-purple: #8e3a9a;
    --accent-green: #8cc63f;
    --accent-orange: #f7a93b;
    --accent-sky: #5ab8e0;
  }
  * { box-sizing: border-box; margin: 0; padding: 0; }
  html, body { width: 1200px; height: 900px; overflow: hidden; }
  body { background: var(--stage); position: relative; }

  .card {
    position: absolute;
    top: 75px;
    width: 460px;
    height: 750px;
    background: var(--paper);
    overflow: hidden;
    box-shadow: 0 6px 24px rgba(0,0,0,0.18);
  }
  .card--front { left: 75px; }
  .card--back { left: 665px; }

  /* Front */
  .front__top {
    position: absolute; inset: 0 0 auto 0; height: 375px;
    display: flex; align-items: center; justify-content: center;
    gap: 14px; padding-top: 170px;
  }
  .front__bottom {
    position: absolute; inset: 375px 0 0 0;
    background: var(--brand-blue);
    display: flex; align-items: center; justify-content: center;
    padding-top: 170px;
  }
  .brand-dot {
    width: 26px; height: 26px; border-radius: 50%;
    background: var(--accent-pink);
  }
  .brand-name {
    font-family: "Ubuntu Condensed", "Arial Narrow", sans-serif;
    font-size: 84px; line-height: 1;
    color: var(--ink);
    letter-spacing: 1px;
  }
  .brand-name--faint { color: var(--deep-blue); }

  /* Back */
  .back__band {
    position: absolute; left: 0; right: 0; top: 300px; height: 390px;
    background: var(--brand-blue);
  }
  .back__decor {
    position: absolute; right: -30px; top: 20px;
    width: 290px; height: 270px; border-radius: 50%;
    background: radial-gradient(circle at 50% 50%, var(--accent-pink) 0%, var(--accent-purple) 30%, var(--accent-sky) 62%, var(--accent-green) 82%, rgba(255,255,255,0) 100%);
    opacity: 0.85;
  }
  .holder-name {
    position: absolute; right: 14px; top: 310px;
    padding: 6px 16px;
    font-family: "Playfair Display", Georgia, serif;
    font-size: 40px; line-height: 1.1; letter-spacing: -1px;
    background: radial-gradient(ellipse at 50% 50%, rgba(255,255,255,0.95) 0%, rgba(255,255,255,0.75) 50%, rgba(255,255,255,0) 75%);
  }
  .holder-name__first { color: var(--ink); }
  .holder-name__last { color: var(--name-blue); margin-left: 4px; }

  .contact-list {
    position: absolute; left: 90px; top: 420px;
    list-style: none;
    font-family: "Varela Round", Arial, sans-serif;
    font-size: 16px; color: var(--accent-yellow);
  }
  .contact-list li {
    display: flex; align-items: center; gap: 8px;
    height: 24px;
  }
  .contact-icon { width: 14px; height: 14px; flex: none; }
  .contact-icon--square { width: 14px; height: 14px; display: flex; align-items: center; justify-content: center; }
  .contact-icon--square::before { content: ""; width: 12px; height: 12px; background: var(--accent-pink); border-radius: 2px; }
</style>
</head>
<body>
  <section class="card card--front">
    <div class="front__top">
      <span class="brand-dot"></span>
      <span class="brand-name">VelloPath</span>
    </div>
    <div class="front__bottom">
      <span class="brand-name brand-name--faint">VelloPath</span>
    </div>
  </section>

  <section class="card card--back">
    <div class="back__band"></div>
    <div class="back__decor" role="img" aria-label="Colourful brand dot decoration area"></div>
    <h1 class="holder-name"><span class="holder-name__first">Name</span><span class="holder-name__last">Surname</span></h1>
    <ul class="contact-list">
      <li>
        <svg class="contact-icon" viewBox="0 0 14 14"><path d="M7 1a4 4 0 0 1 4 4c0 3-4 8-4 8S3 8 3 5a4 4 0 0 1 4-4z" fill="#e8308c"/><circle cx="7" cy="5" r="1.5" fill="#1b95d3"/></svg>
        Adress
      </li>
      <li>
        <svg class="contact-icon" viewBox="0 0 14 14"><path d="M3 1h3l1 3-2 1.5a8 8 0 0 0 3.5 3.5L10 7l3 1v3a2 2 0 0 1-2 2C6 13 1 8 1 3a2 2 0 0 1 2-2z" fill="#e8308c"/></svg>
        Phone number
      </li>
      <li>
        <svg class="contact-icon" viewBox="0 0 14 14"><rect x="1" y="3" width="12" height="8" rx="1" fill="#e8308c"/><path d="M1.5 3.5 7 8l5.5-4.5" stroke="#1b95d3" stroke-width="1" fill="none"/></svg>
        E-mail
      </li>
      <li>
        <svg class="contact-icon" viewBox="0 0 14 14"><circle cx="7" cy="7" r="6" fill="#e8308c"/><path d="M1 7h12M7 1c-3 3-3 9 0 12M7 1c3 3 3 9 0 12" stroke="#1b95d3" stroke-width="0.8" fill="none"/></svg>
        Web
      </li>
      <li>
        <span class="contact-icon contact-icon--square"></span>
        Friendline
      </li>
    </ul>
  </section>
</body>
</html>
```